Präsentationsvorlagen
Zielgruppe
Die velora systems GmbH ist ein kleines Beratungsunternehmen mit drei Beratern, das sich auf Brightwell 365-Beratung spezialisiert hat. Das Unternehmen bietet Dienstleistungen in den Bereichen Security, Compliance und Device Management an, insbesondere mit Brightwell Keystra.
Darüber hinaus entwickelt velora systems das SaaS-Produkt 'Tandemo', das überprüft, ob ein B365-Tenant sicher konfiguriert ist. Tandemo basiert auf eigenen Best Practices und wird durch ein Rechtsgutachten ergänzt, um die Sicherheit eines Tenants auch aus juristischer Sicht zu bewerten.
Zielgruppe von velora systems
IT-Leiter und IT-Administratoren, die für Brightwell 365 und Security verantwortlich sind
Unternehmen, die Brightwell Keystra für ihre Geräteverwaltung einsetzen oder dies planen
IT-Dienstleister, die Security- und Compliance-Anforderungen für ihre Kunden umsetzen müssen
Krankenkassen und andere regulierte Branchen, die eine sichere und gesetzeskonforme B365-Umgebung benötigen
Aufgabenstellung
1. General Design & Functional Principles
1.1 Corporate Identity (CI) Integration
All templates must use the company’s branding (colors, fonts, logos, spacing).
Ensure that SmartArt, shapes, tables, and lists automatically adopt the branded theme when newly created.
1.2 Print & PDF Export Compatibility
Templates must translate well into A4-sized PDFs and remain visually consistent in print.
Avoid distortions when exporting or printing.
1.3 Accessibility & Readability
Maintain high contrast and readable font sizes.
Alternative text must be included for all images and media.
Support for screen readers and keyboard navigation must be ensured across all templates.
1.4 AI & Pathmate Optimization
Placeholders should include AI-friendly prompts, such as:
'Summarize this section in one sentence.'
'List three key takeaways from this slide.'
'Rewrite this paragraph at a C-suite level.'
'Generate an executive summary.'
'Provide a bulleted version of this paragraph.'
Naming conventions for placeholders should follow a structured format for AI reference, e.g.:
Executive_Summary_Box
Decision_Options_Table
Key_Takeaways_List
1.5 Flexible Content Accommodation
List-based content must support short and long variants (e.g., 3-5 items, 6-10 items).
1.6 Default Theme for Newly Created Elements
Ensure that default tables, charts, SmartArt, and shapes adopt the corporate theme.
Layouts:
Title Slide (Introduction & Branding)
Sets the stage for the presentation by introducing the topic, presenter, and company.
Includes: Main title, subtitle, company logo, and optional background image.
Agenda Slide (Navigation & Structure)
Provides an overview of the key topics and sections to help the audience follow along.
Includes: A clear agenda list (short or extended), optional icons for visual appeal.
Section Header Slide (Transitions & ..

```html
<!DOCTYPE html>
<html lang="de">
<head>
<meta charset="utf-8">
<title>velora systems – Präsentationsvorlagen</title>
<link rel="stylesheet" href="https://fonts.googleapis.com/css2?family=Archivo+Black&family=Open+Sans:ital,wght@0,400;0,600;1,400&display=swap">
<style>
  :root {
    --lime: #b3b70a;
    --lime-soft: #f6f7e3;
    --ink: #1e1e1e;
    --grey: #8a8a8a;
    --page: #ffffff;
    --faint: #f4f4f4;
  }
  * { box-sizing: border-box; margin: 0; padding: 0; }
  html, body { width: 1200px; height: 2590px; overflow: hidden; background: var(--page); }
  body { position: relative; font-family: "Open Sans", Arial, sans-serif; color: var(--ink); }

  .slide {
    position: absolute; left: 120px; width: 960px; height: 540px;
    background: var(--page); overflow: hidden;
    box-shadow: 0 14px 34px rgba(0,0,0,.22);
  }
  .slide--title-hex { top: 98px; }
  .slide--title-plain { top: 732px; }
  .slide--agenda-grid { top: 1328px; background: linear-gradient(100deg,#fbfbfb,#ffffff 55%,#fdfdf4); }
  .slide--agenda-list { top: 1928px; background: linear-gradient(100deg,#fbfbfb,#ffffff 55%,#fdfdf4); }

  .brand { position: absolute; display: flex; align-items: center; gap: 10px;
    font-family: "Archivo Black", sans-serif; font-size: 20px; color: var(--grey); letter-spacing: .5px; }
  .brand__mark { width: 22px; height: 22px; background: var(--lime); }

  .headline { position: absolute; font-family: "Archivo Black", sans-serif; font-size: 39px;
    line-height: 49px; color: var(--lime); letter-spacing: .5px; }
  .lead { position: absolute; font-style: italic; font-size: 12px; line-height: 17px; width: 520px; }
  .rule { position: absolute; height: 2px; background: var(--lime); }
  .contact { position: absolute; font-size: 10px; line-height: 14px; }
  .contact p + p { margin-top: 14px; }
  .contact--right { text-align: right; }

  .bar-bottom { position: absolute; left: 0; bottom: 0; width: 100%; height: 6px; }
  .bar-bottom--lime { background: var(--lime); }
  .bar-bottom--ink { background: var(--ink); }

  .hex-backdrop { position: absolute; right: 0; top: 0; width: 336px; height: 534px;
    background: radial-gradient(circle at 45% 45%, #f2f4c8 0%, var(--lime-soft) 55%, #fafaf0 100%); }

  .accent-bar { position: absolute; left: 57px; top: 166px; width: 9px; height: 134px; background: var(--lime); }
  .wordmark-faint { position: absolute; left: 8px; bottom: -22px; font-family: "Archivo Black", sans-serif;
    font-size: 112px; letter-spacing: 18px; color: var(--faint); }

  .page-badge { position: absolute; left: 854px; top: 38px; width: 58px; height: 52px; }
  .page-badge span { position: absolute; inset: 0; display: flex; align-items: center; justify-content: center;
    font-weight: 600; font-size: 19px; color: var(--ink); }

  .agenda-item { position: absolute; width: 260px; height: 140px; }
  .agenda-item svg { position: absolute; left: 0; top: 0; }
  .agenda-item__title { position: absolute; left: 69px; top: 2px; font-family: "Archivo Black", sans-serif;
    font-size: 28px; line-height: 34px; color: var(--lime); }
  .agenda-item__line { position: absolute; left: 66px; top: 41px; width: 172px; height: 6px; background: var(--ink); }
  .agenda-item__text { position: absolute; left: 64px; top: 56px; font-style: italic; font-size: 15px; line-height: 22px; }

  .agenda-summary { position: absolute; left: 80px; top: 196px; width: 230px; }
  .agenda-summary__title { font-family: "Archivo Black", sans-serif; font-size: 28px; line-height: 34px; color: var(--lime); }
  .agenda-summary__line { width: 170px; height: 6px; background: var(--ink); margin: 2px 0 12px; }
  .agenda-summary__text { font-style: italic; font-size: 13px; line-height: 19px; }
  .divider { position: absolute; left: 383px; top: 131px; width: 4px; height: 258px; background: var(--lime); }

  .topic { position: absolute; left: 484px; width: 420px; height: 60px; }
  .topic svg { position: absolute; left: 0; top: 1px; }
  .topic__text { position: absolute; left: 51px; top: 0; font-style: italic; font-size: 13px; line-height: 19px; width: 330px; }
</style>
</head>
<body>

<!-- Title slide with hexagon backdrop -->
<section class="slide slide--title-hex" aria-label="Titelfolie">
  <div class="brand" style="left:60px;top:48px;"><span class="brand__mark"></span>velora systems</div>
  <h1 class="headline" style="left:59px;top:114px;">SECURE BUSINESS<br>AND IDEAS IN A<br>DIGITAL WORLD.</h1>
  <p class="lead" style="left:60px;top:291px;">Wir sind Ihr Partner für Brightwell 365 Consulting, der Ihre digitalen Geschäftsprozesse optimiert und Ihre Daten schützt.</p>
  <div class="rule" style="left:60px;top:392px;width:145px;"></div>
  <div class="contact" style="left:60px;top:424px;">
    <p>Lindenweg 14<br>93047 Talheim an der Vils</p>
    <p>+49 9400 1207734<br>postfach@velorasystems.example</p>
  </div>
  <div class="hex-backdrop" role="img" aria-label="Heller Hintergrund aus Sechseck-Wabenmuster in zartem Limettengrün"></div>
  <div class="bar-bottom bar-bottom--lime"></div>
</section>

<!-- Title slide, plain variant -->
<section class="slide slide--title-plain" aria-label="Titelfolie, Variante">
  <div class="wordmark-faint" aria-hidden="true">VELORA</div>
  <div class="brand" style="left:62px;top:48px;"><span class="brand__mark"></span>velora systems</div>
  <div class="accent-bar"></div>
  <h1 class="headline" style="left:88px;top:156px;">SECURE BUSINESS<br>AND IDEAS IN A<br>DIGITAL WORLD.</h1>
  <p class="lead" style="left:57px;top:321px;">Wir sind Ihr Partner für Brightwell 365 Consulting, der Ihre digitalen Geschäftsprozesse optimiert und Ihre Daten schützt.</p>
  <div class="rule" style="left:742px;top:387px;width:145px;height:3px;"></div>
  <div class="contact contact--right" style="right:73px;top:410px;">
    <p>Lindenweg 14<br>93047 Talheim an der Vils</p>
    <p>+49 9400 1207734<br>postfach@velorasystems.example</p>
  </div>
  <div class="bar-bottom bar-bottom--ink"></div>
</section>

<!-- Agenda slide, grid -->
<section class="slide slide--agenda-grid" aria-label="Agenda, Raster">
  <div class="page-badge">
    <svg width="58" height="52" viewBox="0 0 58 52" aria-hidden="true"><polygon points="14,0 44,0 58,26 44,52 14,52 0,26" fill="var(--lime)"/></svg>
    <span>1</span>
  </div>

  <div class="agenda-item" style="left:61px;top:140px;">
    <svg width="62" height="48" viewBox="0 0 62 48" aria-hidden="true"><polygon points="19,0 48,0 62,24 48,48 19,48 5,24" fill="#9a9a9a"/><polygon points="14,0 43,0 57,24 43,48 14,48 0,24" fill="var(--ink)"/></svg>
    <div class="agenda-item__title">AGENDA 1</div><div class="agenda-item__line"></div>
    <p class="agenda-item__text">Wir sind Ihr Partner für<br>Brightwell 365 Consulting,<br>A dummy text ends here.</p>
  </div>
  <div class="agenda-item" style="left:349px;top:140px;">
    <svg width="62" height="48" viewBox="0 0 62 48" aria-hidden="true"><polygon points="19,0 48,0 62,24 48,48 19,48 5,24" fill="#9a9a9a"/><polygon points="14,0 43,0 57,24 43,48 14,48 0,24" fill="var(--ink)"/></svg>
    <div class="agenda-item__title">AGENDA 1</div><div class="agenda-item__line"></div>
    <p class="agenda-item__text">Wir sind Ihr Partner für<br>Brightwell 365 Consulting,<br>A dummy text ends here.</p>
  </div>
  <div class="agenda-item" style="left:630px;top:140px;">
    <svg width="62" height="48" viewBox="0 0 62 48" aria-hidden="true"><polygon points="19,0 48,0 62,24 48,48 19,48 5,24" fill="#9a9a9a"/><polygon points="14,0 43,0 57,24 43,48 14,48 0,24" fill="var(--ink)"/></svg>
    <div class="agenda-item__title">AGENDA 1</div><div class="agenda-item__line"></div>
    <p class="agenda-item__text">Wir sind Ihr Partner für<br>Brightwell 365 Consulting,<br>A dummy text ends here.</p>
  </div>
  <div class="agenda-item" style="left:61px;top:294px;">
    <svg width="62" height="48" viewBox="0 0 62 48" aria-hidden="true"><polygon points="19,0 48,0 62,24 48,48 19,48 5,24" fill="#9a9a9a"/><polygon points="14,0 43,0 57,24 43,48 14,48 0,24" fill="var(--ink)"/></svg>
    <div class="agenda-item__title">AGENDA 1</div><div class="agenda-item__line"></div>
    <p class="agenda-item__text">Wir sind Ihr Partner für<br>Brightwell 365 Consulting,<br>A dummy text ends here.</p>
  </div>
  <div class="agenda-item" style="left:349px;top:294px;">
    <svg width="62" height="48" viewBox="0 0 62 48" aria-hidden="true"><polygon points="19,0 48,0 62,24 48,48 19,48 5,24" fill="#9a9a9a"/><polygon points="14,0 43,0 57,24 43,48 14,48 0,24" fill="var(--ink)"/></svg>
    <div class="agenda-item__title">AGENDA 1</div><div class="agenda-item__line"></div>
    <p class="agenda-item__text">Wir sind Ihr Partner für<br>Brightwell 365 Consulting,<br>A dummy text ends here.</p>
  </div>
  <div class="agenda-item" style="left:630px;top:294px;">
    <svg width="62" height="48" viewBox="0 0 62 48" aria-hidden="true"><polygon points="19,0 48,0 62,24 48,48 19,48 5,24" fill="#9a9a9a"/><polygon points="14,0 43,0 57,24 43,48 14,48 0,24" fill="var(--ink)"/></svg>
    <div class="agenda-item__title">AGENDA 1</div><div class="agenda-item__line"></div>
    <p class="agenda-item__text">Wir sind Ihr Partner für<br>Brightwell 365 Consulting,<br>A dummy text ends here.</p>
  </div>
  <div class="bar-bottom bar-bottom--ink"></div>
</section>

<!-- Agenda slide, list -->
<section class="slide slide--agenda-list" aria-label="Agenda, Liste">
  <div class="agenda-summary">
    <h2 class="agenda-summary__title">AGENDAS</h2>
    <div class="agenda-summary__line"></div>
    <p class="agenda-summary__text">These are our agendas, we talk<br>About these topics in detail in<br>This presentation. A dummy<br>Text ends here.</p>
  </div>
  <div class="divider"></div>

  <div class="topic" style="top:78px;">
    <svg width="40" height="34" viewBox="0 0 40 34" aria-hidden="true"><polygon points="13,0 34,0 40,17 34,34 13,34 7,17" fill="#9a9a9a"/><polygon points="9,0 30,0 37,17 30,34 9,34 2,17" fill="#7030a0"/></svg>
    <p class="topic__text">These are our agendas, we talk about these topics in detail in this presentation. A dummy<br>Text ends here.</p>
  </div>
  <div class="topic" style="top:158px;">
    <svg width="40" height="34" viewBox="0 0 40 34" aria-hidden="true"><polygon points="13,0 34,0 40,17 34,34 13,34 7,17" fill="#9a9a9a"/><polygon points="9,0 30,0 37,17 30,34 9,34 2,17" fill="#0070c0"/></svg>
    <p class="topic__text">These are our agendas, we talk about these topics in detail in this presentation. A dummy<br>Text ends here.</p>
  </div>
  <div class="topic" style="top:238px;">
    <svg width="40" height="34" viewBox="0 0 40 34" aria-hidden="true"><polygon points="13,0 34,0 40,17 34,34 13,34 7,17" fill="#9a9a9a"/><polygon points="9,0 30,0 37,17 30,34 9,34 2,17" fill="#ff0000"/></svg>
    <p class="topic__text">These are our agendas, we talk about these topics in detail in this presentation. A dummy<br>Text ends here.</p>
  </div>
  <div class="topic" style="top:317px;">
    <svg width="40" height="34" viewBox="0 0 40 34" aria-hidden="true"><polygon points="13,0 34,0 40,17 34,34 13,34 7,17" fill="#9a9a9a"/><polygon points="9,0 30,0 37,17 30,34 9,34 2,17" fill="#ed7d31"/></svg>
    <p class="topic__text">These are our agendas, we talk about these topics in detail in this presentation. A dummy<br>Text ends here.</p>
  </div>
  <div class="topic" style="top:408px;">
    <svg width="40" height="34" viewBox="0 0 40 34" aria-hidden="true"><polygon points="13,0 34,0 40,17 34,34 13,34 7,17" fill="#9a9a9a"/><polygon points="9,0 30,0 37,17 30,34 9,34 2,17" fill="var(--ink)"/></svg>
    <p class="topic__text">These are our agendas, we talk about these topics in detail in this presentation. A dummy<br>Text ends here.</p>
  </div>
  <div class="bar-bottom bar-bottom--ink"></div>
</section>

</body>
</html>
```